Bright Harbor

Looking for a brochure for a childcare center and sales sheet

Target Market(s)

Families
Parents
Summer Campers

Industry/Entity Type

Childcare

Colors
33b8a4
9ccb3b
fbed22
ffc214
f58646

Requirements
Must have
• Bright colors
• Highlight services
Nice to have
• Welcoming front page
• Inside page with reasons to enroll
• We have a website
• www.brightharborlearningcenter.example

```html
<!DOCTYPE html>
<html lang="en">
<head>
<meta charset="utf-8">
<title>Bright Harbor – Childcare Brochure</title>
<link href="https://fonts.googleapis.com/css2?family=Cherry+Swash&family=Montserrat:wght@400;600;700&display=swap" rel="stylesheet">
<style>
:root{
  --backdrop:#a6a7aa;
  --paper:#ffffff;
  --red:#e2403a;
  --teal:#3a97ab;
  --green:#7cb83a;
  --lime:#9ccb3b;
  --yellow:#f4e74a;
  --sun:#fbed22;
  --amber:#ffc214;
  --orange:#e9563c;
  --ink:#2b2b2b;
}
*{margin:0;padding:0;box-sizing:border-box}
html,body{width:1200px;height:1000px;overflow:hidden}
body{background:var(--backdrop);font-family:"Montserrat",Arial,sans-serif;position:relative}
.spread{position:absolute;left:35px;top:100px;width:1130px;height:800px;background:var(--paper);overflow:hidden}
.page{position:absolute;top:0;height:800px;width:565px;overflow:hidden}
.page--back{left:0;background:linear-gradient(180deg,#fdf6ee 0%,#fbeff0 45%,#fff 100%)}
.page--front{left:565px;background:linear-gradient(180deg,#fdf3ee 0%,#fbf7f0 60%,#fff 100%)}
.photo{position:absolute}
.hero-back{left:0;top:0;width:565px;height:277px;
  background:
    radial-gradient(ellipse 60% 45% at 50% 40%,rgba(247,170,185,.55),transparent 70%),
    radial-gradient(ellipse 40% 30% at 30% 85%,rgba(120,150,220,.35),transparent 70%),
    linear-gradient(180deg,#efe3d8 0%,#f2c7cf 45%,#e6d6e4 75%,#f4e6dc 100%)}
.hero-front{left:0;top:0;width:565px;height:235px;
  background:
    radial-gradient(ellipse 35% 50% at 62% 60%,rgba(222,232,70,.7),transparent 70%),
    radial-gradient(ellipse 35% 45% at 22% 70%,rgba(240,160,190,.55),transparent 70%),
    linear-gradient(120deg,#f4d6dc 0%,#f7dccb 45%,#eef0a8 72%,#f6ead0 100%)}
.wave-top{position:absolute;left:0;top:0;width:565px}
.logo{position:absolute;display:flex;align-items:center;gap:6px}
.logo__dot{width:34px;height:34px;border-radius:50%;background:var(--amber)}
.logo__name{font-weight:600;font-size:13px;color:var(--teal);letter-spacing:.3px;line-height:1}
.logo__tag{font-size:5.5px;font-weight:600;color:var(--ink);letter-spacing:.2px;margin-top:3px}
.display{font-family:"Cherry Swash",Georgia,serif;font-weight:400;position:absolute;width:100%;text-align:center;white-space:nowrap}
.back-title{top:384px;font-size:32px;color:var(--red)}
.back-sub{top:440px;font-size:21px;color:var(--teal)}
.card{position:absolute;font-size:11px;line-height:13.5px;color:var(--ink);padding:8px 9px}
.card strong{font-weight:700;display:block;font-size:10.5px}
.card p{margin-top:12px;white-space:nowrap}
.card .mail{font-size:10px;letter-spacing:-.1px}
.card--wantage{left:27px;top:487px;width:274px;height:91px;background:var(--yellow)}
.card--hours{left:360px;top:487px;width:130px;height:91px;background:var(--orange);color:#fff}
.card--hours h3{font-size:11px;font-weight:700;margin-bottom:10px}
.card--union{left:258px;top:593px;width:280px;height:100px;background:var(--yellow);border:4px solid #fff}
.kids-strip{position:absolute;left:70px;top:735px;width:420px;height:45px;border-radius:20px;background:linear-gradient(90deg,#f7e07a,#f6c9a6,#d6e78c,#f7e07a);opacity:.55}
.front-logo{left:200px;top:22px}
.band{position:absolute;left:0;top:238px;width:565px;height:58px;background:rgba(255,255,255,.92)}
.front-title{top:250px;font-size:29px;color:var(--red)}
.rule{position:absolute;left:0;top:302px;width:565px;height:8px;background:linear-gradient(90deg,var(--amber),var(--sun),var(--lime))}
.faint{position:absolute;left:0;top:310px;width:565px;height:275px;background:linear-gradient(180deg,#f8efe4,#fbf4ee);opacity:.8}
.front-sub{top:326px;font-size:23px;color:var(--green)}
.circle{position:absolute;width:112px;height:112px;border-radius:50%;border:3px solid var(--amber)}
.c1{left:25px;top:367px;background:radial-gradient(circle at 40% 40%,#f6dccb,#e28a7a 60%,#f0e4cf)}
.c2{left:158px;top:443px;background:radial-gradient(circle at 55% 40%,#f6e6da,#d9c2b2 55%,#7c9a58)}
.c3{left:291px;top:366px;background:radial-gradient(circle at 45% 45%,#f0b7cc,#e26a96 55%,#9a8aa0)}
.c4{left:426px;top:443px;background:linear-gradient(180deg,#eee0d6 0%,#d7bcd2 50%,#92c45e 100%)}
.section-head{position:absolute;top:584px;width:100%;text-align:center;font-weight:700;font-size:19px;color:var(--teal);letter-spacing:.3px}
.body-copy{position:absolute;left:28px;top:620px;width:512px;font-size:10.9px;line-height:14.4px;color:var(--ink);text-align:justify}
.wave-bottom{position:absolute;left:0;bottom:0;width:565px}
</style>
</head>
<body>
<main class="spread">

  <section class="page page--back">
    <div class="photo hero-back" role="img" aria-label="Photo of smiling preschool children raising paper shapes above a craft table"></div>
    <svg class="wave-top" viewBox="0 0 565 60" height="60" aria-hidden="true">
      <path d="M0 0H565V40C470 10 380 45 280 30C170 14 90 40 0 20Z" fill="#fdf8f2" opacity=".85"/>
      <path d="M0 20C90 40 170 14 280 30C380 45 470 10 565 40" fill="none" stroke="#f4e74a" stroke-width="3"/>
    </svg>

    <div class="logo" style="left:203px;top:312px">
      <span class="logo__dot"></span>
      <div><div class="logo__name">BRIGHT HARBOR</div><div class="logo__tag">EARLY LEARNING CHILDCARE CENTER</div></div>
    </div>

    <h1 class="display back-title">Get Pricing &amp; Program Info</h1>
    <h2 class="display back-sub">Contact Your Local Daycare</h2>

    <div class="card card--wantage">
      <strong>Wantage, NJ</strong>
      <strong>27 Meadow Lark Rd. Wantage, NJ 07400</strong>
      <p>Phone: (555) 014-2080<br><span class="mail">Email: info@brightharborlearningcenter.example</span></p>
    </div>
    <div class="card card--hours">
      <h3>BUSINESS HOURS</h3>
      Mo<br>6:30pm – 6:30pm<br>Tu, We, Th, Fr<br>6:30am – 6:30pm
    </div>

    <svg class="wave-bottom" viewBox="0 0 565 150" height="150" aria-hidden="true">
      <path d="M0 30C120 0 250 10 380 50C460 75 520 80 565 78V150H0Z" fill="#f6e93f"/>
      <path d="M0 30C120 0 250 10 380 50C460 75 520 80 565 78" fill="none" stroke="#8cc63f" stroke-width="4"/>
    </svg>
    <div class="kids-strip" role="img" aria-label="Row of cartoon children playing with a kite, balloon and jump rope"></div>

    <div class="card card--union">
      <strong>Union, NJ</strong>
      <strong>118 Willow Crest Ave. Union, NJ 07000</strong>
      <p>Phone: (555) 014-2080<br><span class="mail">Email: info@brightharborlearningcenter.example</span></p>
    </div>
  </section>

  <section class="page page--front">
    <div class="photo hero-front" role="img" aria-label="Photo of a young girl drawing with coloured pencils beside sea-themed doodles"></div>
    <svg class="wave-top" viewBox="0 0 565 90" height="90" aria-hidden="true">
      <path d="M0 0H565V8C470 10 400 40 300 70C200 95 100 85 0 60Z" fill="#fdf8f2"/>
      <path d="M0 60C100 85 200 95 300 70C400 40 470 10 565 8" fill="none" stroke="#f4e74a" stroke-width="3"/>
    </svg>
    <div class="logo front-logo">
      <span class="logo__dot"></span>
      <div><div class="logo__name">BRIGHT HARBOR</div><div class="logo__tag">EARLY LEARNING CHILDCARE CENTER</div></div>
    </div>

    <div class="band"></div>
    <h1 class="display front-title">Top Rated Hometown Child Care</h1>
    <div class="rule"></div>
    <div class="faint" role="img" aria-label="Faded background photo of children in a classroom"></div>
    <h2 class="display front-sub">Serving The Families Of Union, New Jersey</h2>

    <div class="circle c1" role="img" aria-label="Photo of two girls playing with toys"></div>
    <div class="circle c2" role="img" aria-label="Photo of a child playing a board game"></div>
    <div class="circle c3" role="img" aria-label="Photo of a child on a playground swing"></div>
    <div class="circle c4" role="img" aria-label="Photo of two sisters sitting on grass"></div>

    <h3 class="section-head">QUALITY DAY CARE IN UNION, NJ</h3>
    <p class="body-copy">As a day care in Union, Bright Harbor Learning Center aims to provide the warmth and personal touch that your child needs. This is done with a family-friendly and safe place to explore and learn through multiple methods. With small classes of usually 10-14 children per class and the guidance of experienced caregivers and teachers, we encourage our students to participate actively in an educational experience. This promotes learning, self-reliance and exploration in thinking. Our goal as a childcare center is to provide positive and enriching experiences as your child learns and grows.</p>

    <svg class="wave-bottom" viewBox="0 0 565 62" height="62" aria-hidden="true">
      <path d="M0 12C120 2 250 2 360 16C450 28 520 30 565 28V62H0Z" fill="#f6e93f"/>
      <path d="M0 12C120 2 250 2 360 16C450 28 520 30 565 28" fill="none" stroke="#8cc63f" stroke-width="4"/>
    </svg>
  </section>

</main>
</body>
</html>
```